Bierlogo gesucht
Zielgruppe
Bierherstellung / Zielgruppe sowohl Konsumenten von traditionellen Sorten als auch Liebhaber von Craftbeer
Aufgabenstellung
Aufgabe ist die Gestaltung eines Bieretiketts für den Brustbereich der Flasche / Weitere Auftragserweiterung Website und Cooperate Identity gewünscht / Lebensmittelrechtlich relevante Angaben sind zu berücksichtigen / Herstellung im Raum Oberbayern - Ammersee
Logo in Verbindung mit dem Namen "Haldbrunner" soll sowohl Qualität als auch Offenheit für neue Einflüsse, Rezepte, Inhaltsstoffe vermitteln, Stil kann gerne sehr einfach bzgl. Farbgebung aber einprägsam sein

```html
<!DOCTYPE html>
<html lang="de">
<head>
<meta charset="utf-8">
<title>Haldbrunner Beer – Etiketten</title>
<link rel="stylesheet" href="https://fonts.googleapis.com/css2?family=Big+Shoulders+Stencil+Display:wght@800;900&family=Krona+One&family=Open+Sans:wght@400&display=swap">
<style>
  :root {
    --canvas: #ffffff;
    --label-edge: #231f20;
    --gold: #b9a55a;
    --panel: #231f20;
    --white: #ffffff;
    --blue: #1ba3de;
    --orange: #f4a13a;
    --hop: #a6c73a;
    --wing: #f3efe0;
    --rock: #8c8c8c;
  }
  * { margin: 0; padding: 0; box-sizing: border-box; }
  html, body {
    width: 1200px; height: 900px; overflow: hidden;
    background: var(--canvas);
  }
  .canvas { position: relative; width: 1200px; height: 900px; }

  .label {
    position: absolute; top: 160px;
    width: 484px; height: 563px;
    background: var(--white);
    border: 2px solid var(--label-edge);
  }
  .label--pale { left: 90px; --accent: var(--blue); }
  .label--helles { left: 625px; --accent: var(--orange); }

  .label__frame {
    position: absolute; inset: 9px;
    background: var(--panel);
    border: 6px solid var(--gold);
    overflow: hidden;
  }

  .ingredients {
    position: absolute; left: 14px; top: 12px;
    font: 400 9px/1.25 "Open Sans", sans-serif;
    color: var(--gold);
  }
  .volume {
    position: absolute; right: 12px; top: 12px;
    font: 400 20px/1 "Open Sans", sans-serif;
    color: var(--gold);
  }
  .claim {
    position: absolute; left: 0; right: 0; top: 14px;
    text-align: center;
    font: 800 25px/1.05 "Big Shoulders Stencil Display", sans-serif;
    font-variant: small-caps;
    letter-spacing: 0.5px;
    color: var(--accent);
  }
  .brand {
    position: absolute; left: 0; right: 0; top: 60px;
    text-align: center;
    font: 900 78px/80px "Big Shoulders Stencil Display", sans-serif;
    color: var(--white);
    letter-spacing: 1px;
    z-index: 2;
  }
  .emblem {
    position: absolute; left: 54px; top: 222px;
    width: 345px; height: 122px;
    border-radius: 60px 60px 80px 80px;
    background: radial-gradient(ellipse at center, var(--hop) 0 22%, var(--wing) 23% 60%, rgba(243,239,224,0) 75%);
    z-index: 1;
  }
  .mountains {
    position: absolute; left: 28px; top: 370px;
    width: 401px; height: 50px;
    background: linear-gradient(180deg, #ffffff 0%, #cfcfcf 45%, var(--rock) 100%);
    border-radius: 40px 40px 2px 2px;
  }
  .rule {
    position: absolute; height: 2px; background: var(--blue);
  }
  .rule--long { left: 62px; top: 427px; width: 336px; }
  .rule--short { left: 130px; top: 436px; width: 141px; }

  .variety {
    position: absolute; left: 0; right: 0; top: 455px;
    display: flex; align-items: center; justify-content: center; gap: 8px;
  }
  .variety__ornament {
    width: 44px; height: 10px; border-radius: 5px;
    background: var(--gold);
  }
  .variety__dash { width: 10px; height: 2px; background: var(--gold); }
  .variety__name {
    font: 400 22px/1 "Krona One", sans-serif;
    color: var(--accent);
    letter-spacing: 2px;
    padding: 0 4px;
  }

  .best-before, .origin {
    position: absolute; top: 520px;
    font: 400 9px/1 "Open Sans", sans-serif;
    color: var(--gold);
  }
  .best-before { left: 14px; }
  .origin { left: 190px; }
  .alcohol {
    position: absolute; right: 12px; top: 511px;
    font: 400 17px/1 "Open Sans", sans-serif;
    color: var(--gold);
  }
</style>
</head>
<body>
<main class="canvas">

  <article class="label label--pale">
    <div class="label__frame">
      <p class="ingredients">Zutaten:<br>Wasser,<br>Gerstenmalz,<br>Hopfen</p>
      <p class="volume">e 50cl</p>
      <p class="claim">Really crafted<br>by hand</p>
      <h1 class="brand">HALDBRUNNER<br>BEER</h1>
      <div class="emblem" role="img" aria-label="Geflügelte Hopfendolde in Grün mit weißen Flügeln"></div>
      <div class="mountains" role="img" aria-label="Alpenpanorama mit schneebedeckten Gipfeln"></div>
      <div class="rule rule--long"></div>
      <div class="rule rule--short"></div>
      <div class="variety">
        <span class="variety__ornament" role="img" aria-label="Gerstenähre"></span>
        <span class="variety__dash"></span>
        <span class="variety__name">PALE ALE</span>
        <span class="variety__dash"></span>
        <span class="variety__ornament" role="img" aria-label="Gerstenähre"></span>
      </div>
      <p class="best-before">mindestens haltbar bis:</p>
      <p class="origin">86999-Talbach</p>
      <p class="alcohol">Alk.: 5,0% vol</p>
    </div>
  </article>

  <article class="label label--helles">
    <div class="label__frame">
      <p class="ingredients">Zutaten:<br>Wasser,<br>Gerstenmalz,<br>Hopfen</p>
      <p class="volume">e 50cl</p>
      <p class="claim">Really crafted<br>by hand</p>
      <h1 class="brand">HALDBRUNNER<br>BEER</h1>
      <div class="emblem" role="img" aria-label="Geflügelte Hopfendolde in Grün mit weißen Flügeln"></div>
      <div class="mountains" role="img" aria-label="Alpenpanorama mit schneebedeckten Gipfeln"></div>
      <div class="rule rule--long"></div>
      <div class="rule rule--short"></div>
      <div class="variety">
        <span class="variety__ornament" role="img" aria-label="Gerstenähre"></span>
        <span class="variety__dash"></span>
        <span class="variety__name">HELLES</span>
        <span class="variety__dash"></span>
        <span class="variety__ornament" role="img" aria-label="Gerstenähre"></span>
      </div>
      <p class="best-before">mindestens haltbar bis:</p>
      <p class="origin">86999-Talbach</p>
      <p class="alcohol">Alk.: 5,0% vol</p>
    </div>
  </article>

</main>
</body>
</html>
```